The Hidden Storm Beneath Your Garden Book Cover

Need a book cover that jumps out, simple is good. I am trying to relay to readers that they face a serious tax burden when they reach retirement.

I am attaching the cover I've been using, which I designed, but it's not nearly effective enough.
Get rid of the word "Accounts" in the cover, please.

```html
<!DOCTYPE html>
<html lang="en">
<head>
<meta charset="utf-8">
<title>The Hidden Storm Beneath Your Garden — Book Cover</title>
<link rel="stylesheet" href="https://fonts.googleapis.com/css2?family=Montserrat:wght@400;700;800&display=swap">
<style>
  :root {
    --paper: #ffffff;
    --alarm-red: #e8130f;
    --ink: #0d0d0d;
    --cube-light: #f2403a;
    --cube-mid: #d90e0b;
    --cube-dark: #9e0806;
    --author-white: #ffffff;
  }
  html, body {
    margin: 0;
    padding: 0;
    width: 800px;
    height: 1200px;
    overflow: hidden;
    background: var(--paper);
  }
  .cover {
    position: relative;
    width: 800px;
    height: 1200px;
    background: var(--paper);
    overflow: hidden;
    font-family: "Montserrat", sans-serif;
  }
  .cover-title {
    position: absolute;
    left: 0;
    top: 0;
    width: 800px;
    height: 280px;
    margin: 0;
  }
  .title-line {
    font-family: "Montserrat", sans-serif;
    font-weight: 800;
  }
  .title-line--red { fill: var(--alarm-red); }
  .title-line--black { fill: var(--ink); }
  .subtitle {
    position: absolute;
    top: 243px;
    left: 0;
    width: 800px;
    margin: 0;
    text-align: center;
    font-family: "Montserrat", sans-serif;
    font-weight: 400;
    font-size: 22px;
    letter-spacing: -0.2px;
    color: var(--ink);
  }
  .cube-stack {
    position: absolute;
    left: 0;
    top: 320px;
    width: 800px;
    height: 880px;
  }
  .author-name {
    font-family: "Montserrat", sans-serif;
    font-weight: 700;
    font-size: 44px;
    fill: var(--author-white);
  }
</style>
</head>
<body>
  <main class="cover">
    <h1 class="cover-title">
      <svg width="800" height="280" viewBox="0 0 800 280" aria-label="The Hidden Storm Beneath Your Garden">
        <text class="title-line title-line--red" x="44" y="132" font-size="86" textLength="712" lengthAdjust="spacingAndGlyphs">THE HIDDEN STORM</text>
        <text class="title-line title-line--black" x="50" y="220" font-size="78" textLength="700" lengthAdjust="spacingAndGlyphs">BENEATH YOUR GARDEN</text>
      </svg>
    </h1>
    <p class="subtitle">AND HOW THE ROTH IRA VAN HELP YOU AVOID IT</p>

    <svg class="cube-stack" width="800" height="880" viewBox="0 0 800 880">
      <defs>
        <linearGradient id="cubeShade" x1="0" y1="0" x2="1" y2="1">
          <stop offset="0" stop-color="var(--cube-light)"/>
          <stop offset="0.55" stop-color="var(--cube-mid)"/>
          <stop offset="1" stop-color="var(--cube-dark)"/>
        </linearGradient>
      </defs>
      <polygon role="img" aria-label="Stacked glossy red cubes printed with white percent signs"
        fill="url(#cubeShade)"
        points="0,200 120,250 190,320 230,100 310,12 520,160 610,330 700,228 800,260 800,880 0,880"/>
      <text class="author-name" transform="translate(400 740) rotate(13)" text-anchor="middle">JESSE MARLOWE</text>
    </svg>
  </main>
</body>
</html>
```